VORTEK Studio Shape your ideas

VORTEK Studio is a soci% 26 # 233; t% 26 # 233; of mobile application design and multiexperience destiny% 26 # 233; % 26 # 224; The% 26 # 39; industry and particularly the watch industry% 26 # 232; re. By multiexperience, I mean applications usable on watches,% 26 # 233; holographic screens,% 26 # 233; touch screens g% 26 # 233; ant, r% 26 # 233; alit% 26 # 233; virtual,% 26 # 224; distance with a gripsense and% 26 # 233; obviously on mobile on tablet and smartphone. Applications will call% 26 # 224; 3d, artificial intelligence, big data. The company logo% 26 # 233; t% 26 # 233; is attached% 26 # 233; below.

Target Market(s)

Swiss precision industry Watchmaking industry% 26 # 232; re

Coding

Coded - Design and coding required

Font styles to use
Sans Serif

Colors

Designer to choose colors to be used in the design.

Requirements
Must have
• A Contact form A gallery of Vid% 26 # 233; o / Photo (portfolio) 3D images of% 26 # 39; illustration orient% 26 # 233; es industry but% 26 # 233; also luxury (take free images A partner page
Nice to have
• A blog
Should not have
• The designs are too loaded, the page should load quickly.

```html
<!DOCTYPE html>
<html lang="en">
<head>
<meta charset="utf-8">
<title>VORTEK Studio — Shape your ideas</title>
<link href="https://fonts.googleapis.com/css2?family=Maven+Pro:wght@400;500;700&display=swap" rel="stylesheet">
<style>
:root{
  --brand-blue:#0a72c4;
  --page-grey:#d8d8d8;
  --white:#ffffff;
  --ink-dark:#2a2a2a;
  --field-hint:#a9b3bd;
}
*{box-sizing:border-box;margin:0;padding:0}
html,body{width:1200px;height:3113px;overflow:hidden}
body{position:relative;background:var(--page-grey);font-family:"Maven Pro",sans-serif;color:var(--white)}
.abs{position:absolute}

/* hero */
.hero{left:0;top:0;width:1200px;height:807px;
  background:radial-gradient(ellipse at 55% 45%,#6d5a4a 0%,#4b4a55 40%,#3a3e4d 75%,#2f3340 100%)}
.hero-shade{left:0;top:0;width:1200px;height:807px;background:rgba(40,45,70,.35)}
.brand{display:flex;align-items:center;gap:8px;font-weight:500;font-size:19px;letter-spacing:1px}
.brand-mark{width:14px;height:14px;background:currentColor}
.brand-top{left:115px;top:42px;color:var(--white)}
.main-nav{right:112px;top:46px;display:flex;gap:16px;font-size:11px;font-weight:500;letter-spacing:.2px}
.hero-title{left:0;width:1200px;top:292px;text-align:center;font-size:44px;line-height:39px;font-weight:500;letter-spacing:.5px}
.hero-sub{left:0;width:1200px;top:380px;text-align:center;font-size:19px;letter-spacing:.5px}
.btn-hero{left:509px;top:431px;width:181px;height:41px;background:var(--brand-blue);font-size:13px;display:flex;align-items:center;justify-content:center;letter-spacing:.3px}

/* feature rows */
.feature-panel{width:324px;height:348px;background:var(--brand-blue);padding:46px 0 0 40px}
.feature-title{font-size:18px;font-weight:500;letter-spacing:.4px;line-height:22px}
.feature-sub{font-size:13px;line-height:16px;margin-top:-2px}
.feature-rule{width:57px;height:2px;background:var(--white);margin:19px 0 22px}
.feature-text{font-size:14px;line-height:17px;width:250px}
.feature-text b{font-weight:700}
.btn-outline{display:flex;align-items:center;justify-content:center;width:147px;height:41px;margin-top:30px;background:var(--white);color:var(--brand-blue);font-size:13px;border:1px solid #c9d7e4}
.photo{width:649px;height:348px}

/* gallery */
.tile{width:324px;height:226px}

/* contact */
.contact{left:114px;top:2348px;width:974px;height:550px;background:var(--brand-blue)}
.field{left:311px;width:351px;background:var(--white);color:var(--field-hint);font-size:12px;padding-left:26px;display:flex;align-items:center}
.field-message{align-items:flex-start;padding-top:20px}
.btn-contact{left:311px;top:417px;width:351px;height:47px;border:1px solid #cfe1f2;font-size:13px;font-weight:500;display:flex;align-items:center;justify-content:center}

/* footer */
.brand-foot{left:0;width:1200px;top:2988px;justify-content:center;color:var(--brand-blue)}
.copyright{left:0;width:1200px;top:3036px;text-align:center;font-size:13px;color:var(--ink-dark)}
</style>
</head>
<body>

<header>
  <div class="abs hero" role="img" aria-label="Smartphone on a table with a castle on a wooded hill rising from its screen"></div>
  <div class="abs hero-shade"></div>
  <div class="abs brand brand-top"><span class="brand-mark"></span>VORTEK Studio</div>
  <nav class="abs main-nav"><span>ABOUT</span><span>TECHNOLOGY</span><span>BLOG</span><span>CONTACT</span></nav>
  <h1 class="abs hero-title">A NEW STANDARD<br>OF PRECISION AND INNOVATION</h1>
  <p class="abs hero-sub">MAKING QUALITY THROUGH EXPERIENCE</p>
  <div class="abs btn-hero">LEARN MORE</div>
</header>

<section>
  <div class="abs feature-panel" style="left:115px;top:626px">
    <h2 class="feature-title">ABOUT VORTEK STUDIO</h2>
    <p class="feature-sub">SWISS PRECISION</p>
    <div class="feature-rule"></div>
    <p class="feature-text">Lorem ipsum dolor sit amet, consec-tetur adipiscing elit, sed do eiusmod tempor incididunt <b>ut labore et dolore magna aliqua.</b> Ut enim ad minim veniam, quis nostrud exercita-tion ullamco laboris nisi ut aliquip.</p>
    <div class="btn-outline">READ MORE</div>
  </div>
  <div class="abs photo" style="left:439px;top:626px;background:linear-gradient(135deg,#3c3a38 0%,#c9c6c2 35%,#f3a25f 55%,#e9893e 70%,#4a4846 100%)" role="img" aria-label="Smartphone with an orange music app screen and earphones on dark wood"></div>

  <div class="abs photo" style="left:115px;top:974px;background:linear-gradient(120deg,#8a5a3e 0%,#b7825f 30%,#1d2228 50%,#8b6049 75%,#c79a7b 100%)" role="img" aria-label="Wrist wearing a smartwatch showing a weather dial"></div>
  <div class="abs feature-panel" style="left:764px;top:974px">
    <h2 class="feature-title">HIGH-END TECHNOLOGY</h2>
    <p class="feature-sub">FOCUSING ON THE INDUSTRY</p>
    <div class="feature-rule"></div>
    <p class="feature-text">Lorem ipsum dolor sit amet, consec-tetur adipiscing elit, sed do eiusmod tempor incididunt <b>ut labore et dolore magna aliqua.</b> Ut enim ad minim veniam, quis nostrud exercita-tion ullamco laboris nisi ut aliquip.</p>
    <div class="btn-outline">READ MORE</div>
  </div>

  <div class="abs feature-panel" style="left:115px;top:1322px">
    <h2 class="feature-title">INTERNATIONAL REACH</h2>
    <p class="feature-sub">CONNECTING WITH THE WORLD</p>
    <div class="feature-rule"></div>
    <p class="feature-text">Lorem ipsum dolor sit amet, consec-tetur adipiscing elit, sed do eiusmod tempor incididunt <b>ut labore et dolore magna aliqua.</b> Ut enim ad minim veniam, quis nostrud exercita-tion ullamco laboris nisi ut aliquip.</p>
    <div class="btn-outline">READ MORE</div>
  </div>
  <div class="abs photo" style="left:439px;top:1322px;background:linear-gradient(160deg,#9fb0c4 0%,#d8e0ea 40%,#7d8ea5 70%,#c5d0dd 100%)" role="img" aria-label="Earth seen from orbit covered in clouds"></div>
</section>

<section aria-label="Portfolio gallery">
  <div class="abs tile" style="left:115px;top:1671px;background:linear-gradient(135deg,#9fb3c6,#2f86c9 70%,#1b5fa0)" role="img" aria-label="Hand setting a smartwatch"></div>
  <div class="abs tile" style="left:439px;top:1671px;background:linear-gradient(135deg,#f2f2f2,#cfcfcf 60%,#3a3a3e)" role="img" aria-label="Laptop and headphones on a white desk"></div>
  <div class="abs tile" style="left:764px;top:1671px;background:linear-gradient(135deg,#c9b6a6,#9a6c47 60%,#5c3d25)" role="img" aria-label="Person typing on a laptop at a wooden table"></div>

  <div class="abs tile" style="left:115px;top:1897px;background:linear-gradient(180deg,#d9c6b6,#a89c93 55%,#6b6a6a)" role="img" aria-label="Hand photographing the sea at sunset with a phone"></div>
  <div class="abs tile" style="left:439px;top:1897px;background:linear-gradient(135deg,#1d2430,#3a4352 55%,#a8b1bd)" role="img" aria-label="Hand holding a dark smartphone"></div>
  <div class="abs tile" style="left:764px;top:1897px;background:radial-gradient(circle at 45% 60%,#1f3b6b,#14161c 55%,#6d6640)" role="img" aria-label="Phone camera capturing a city at night"></div>

  <div class="abs tile" style="left:115px;top:2123px;background:radial-gradient(circle at 50% 50%,#4e7a3e,#1f3660 50%,#0e1326)" role="img" aria-label="Glowing network globe in space"></div>
  <div class="abs tile" style="left:439px;top:2123px;background:linear-gradient(135deg,#8fb84a,#f1e9e2 30%,#27232a 55%,#d8b98b 80%,#f4f4f4)" role="img" aria-label="Fingers touching a gold smartphone screen"></div>
  <div class="abs tile" style="left:764px;top:2123px;background:radial-gradient(circle at 50% 40%,#f3a43a,#6a3a10 30%,#141414 65%)" role="img" aria-label="Glowing light bulb on a dark background"></div>
</section>

<section class="abs contact" aria-label="Contact form">
  <div class="abs field" style="top:88px;height:47px">YOUR NAME</div>
  <div class="abs field" style="top:152px;height:48px">YOUR EMAIL</div>
  <div class="abs field field-message" style="top:216px;height:185px">MESSAGE</div>
  <div class="abs btn-contact">CONTACT US</div>
</section>

<footer>
  <div class="abs brand brand-foot"><span class="brand-mark"></span>VORTEK Studio</div>
  <p class="abs copyright">2020 ©</p>
</footer>

</body>
</html>
```